Product label design needed for an odor removal line of products.

I need a label designed for an odor removal product line. There are eight additional odor removal products that I will need labels designed for so the winner will have additional work from me. I would like each of those products to have a similar look and feel in each one. This contest is for one of the products. The Brightwell 417 (would love a better name if you are so inclined -many people know what it is by the 417). The no smell formula does not mask odors, it eliminates odors at their source . Also Reduces Allergens! Simply open silver packet and place in dispenser. Great for use in cars, near pet beds or litter boxes, near diaper pails -anywhere odors are a problem. Lasts 60-90 days. Safe to use. Other uses: Nursing homes, hotel rooms, locker rooms, teenage boy rooms, basements... Eco Friendly! No VOC's or phthalates! Do not consume. Keep out of reach of children and pets. Replace every 60-90 days. I put the picture of my logo , the product as it is packaged and a picture of the actual product and the dispenser it will go in. the package is 4x5 in silver packet with .25 seam on the side and .5 seam on the top and bottom. (Dispenser will have a label with reorder information on it. to be designed later) You do not have to put all information provided on the label. It is to be used as you see fit. I tend to like clean, bold designs but am open to all options. Prefer not to use word air freshener.

Target Market(s)

Men and women between 30-65

Industry/Entity Type

Cleaning Product

Font styles to use
Sans Serif

Colors
acd136
9bcb3c
ffffff

Requirements
Must have
• ability for concept/look to be used for a laundry product, smaller odor elimination pouch, odor removing canister and spray as well
Nice to have
• I like greens but am open to designers to decide
Should not have
• word air freshener

```html
<!DOCTYPE html>
<html lang="en">
<head>
<meta charset="utf-8">
<title>Brightwell 417 Label</title>
<link rel="stylesheet" href="https://fonts.googleapis.com/css2?family=Montserrat:wght@700;800;900&family=Arimo:wght@400;700&display=swap">
<style>
  :root {
    --page: #ececec;
    --teal: #17987a;
    --lime: #8cc63f;
    --white: #ffffff;
    --orange: #f37021;
    --ink: #111111;
    --photo: #e4e4e1;
  }
  html, body {
    margin: 0;
    width: 1200px;
    height: 1173px;
    overflow: hidden;
    background: var(--page);
  }
  .label {
    position: absolute;
    left: 0; top: 0;
    width: 426px;
    height: 480px;
    transform-origin: 0 0;
    transform: translate(110px, 34px) scale(2.3);
    background: var(--white);
    border-radius: 4px;
    overflow: hidden;
    font-family: "Arimo", Arial, sans-serif;
    color: var(--ink);
  }
  .label > * { position: absolute; }
  .waves { left: 0; top: 0; width: 426px; height: 480px; }
  .brand {
    left: 18px; top: 10px; width: 96px; height: 96px;
    display: flex; flex-direction: column; align-items: center; justify-content: center; gap: 6px;
  }
  .brand-dot { width: 38px; height: 38px; border-radius: 50%; background: var(--lime); }
  .brand-name {
    font-family: "Montserrat", Arial, sans-serif; font-weight: 800;
    font-size: 10.5px; letter-spacing: .5px; color: var(--white);
  }
  .headline {
    left: 125px; top: 12px; width: 296px; margin: 0; text-align: center;
    font-family: "Montserrat", Arial, sans-serif; font-weight: 800;
    font-size: 16px; line-height: 25px; color: var(--white);
  }
  .product-photo {
    left: 56px; top: 126px; width: 137px; height: 133px;
    background: linear-gradient(160deg, #f6f6f4, var(--photo));
    border-radius: 6px;
  }
  .product-name { left: 196px; top: 98px; width: 200px; margin: 0; text-align: center; }
  .product-name .word {
    display: block;
    font-family: "Montserrat", Arial, sans-serif; font-weight: 900;
    font-size: 26px; line-height: 36px; color: var(--orange);
    text-shadow: 2px 2px 0 var(--ink);
  }
  .product-name .number {
    display: block;
    font-family: "Montserrat", Arial, sans-serif; font-weight: 900;
    font-size: 28px; line-height: 34px; color: var(--ink); margin-top: 6px;
  }
  .tagline {
    left: 200px; top: 206px; width: 192px; margin: 0; text-align: center;
    font-weight: 700; font-size: 13.5px; line-height: 16px;
  }
  .step {
    top: 270px; height: 86px;
    border: 2px solid var(--orange); box-sizing: border-box;
    font-weight: 700; font-size: 10px; padding: 2px 4px;
  }
  .step-one { left: 16px; width: 94px; }
  .step-two { left: 125px; width: 66px; }
  .step-art { display: block; margin: 12px auto 0; width: 66px; height: 40px; background: #f1f1f1; }
  .step-note { margin: 14px 0 0 8px; font-size: 10px; line-height: 13px; }
  .uses {
    left: 228px; top: 263px; margin: 0; padding: 0; list-style: none;
    font-weight: 700; font-size: 12.5px; line-height: 16.5px;
  }
  .uses li.indent { padding-left: 22px; }
  .directions {
    left: 30px; top: 358px; width: 190px; margin: 0;
    font-size: 12.5px; line-height: 13.5px;
  }
  .seal {
    left: 342px; top: 399px; width: 65px; height: 65px; box-sizing: border-box;
    border-radius: 50%; background: var(--white); border: 3px solid var(--orange);
  }
  .fine-print {
    left: 28px; top: 444px; margin: 0;
    font-weight: 700; font-size: 10.5px; line-height: 15px; color: var(--white);
  }
</style>
</head>
<body>
  <main class="label">
    <svg class="waves" viewBox="0 0 426 480" aria-hidden="true">
      <path d="M0 0 H426 V72 C330 74 230 92 130 124 C80 140 35 150 0 152 Z" fill="var(--teal)"/>
      <path d="M0 160 C35 158 80 148 130 132 C230 100 330 82 426 80" fill="none" stroke="var(--lime)" stroke-width="5"/>
      <path d="M0 443 C180 443 320 425 426 352 V480 H0 Z" fill="var(--teal)"/>
      <path d="M0 436 C180 436 320 418 426 345" fill="none" stroke="var(--lime)" stroke-width="5"/>
    </svg>

    <div class="brand">
      <span class="brand-dot"></span>
      <span class="brand-name">GREENHAVEN</span>
    </div>

    <p class="headline">THE NO SMELL FORMULA<br>ALSO REDUCES ALERGENS!</p>

    <div class="product-photo" role="img" aria-label="Photo of the white odor eliminating pad"></div>

    <h1 class="product-name">
      <span class="word">BRIGHTWELL</span>
      <span class="number">417</span>
    </h1>

    <p class="tagline">does not mask odors,<br>it eliminates odors<br>at their source.</p>

    <div class="step step-one">step 1
      <span class="step-art" role="img" aria-label="Sketch of the open silver packet"></span>
    </div>
    <div class="step step-two">step 2
      <p class="step-note">dispenser<br>image</p>
    </div>

    <ul class="uses">
      <li>Great for use:</li>
      <li>- in car</li>
      <li>- near pet beds or</li>
      <li class="indent">litter boxes</li>
      <li>- near diaper pails</li>
      <li>- anywhere odors are</li>
      <li class="indent">a problem.</li>
    </ul>

    <p class="directions">So easy&nbsp; and safe to use<br>simply open silver packet<br>and place in dispenser.<br>Lasts 60 -90 days.</p>

    <div class="seal"></div>

    <p class="fine-print">Eco Friendly! No VOC's or phthalates!<br>Do not consume. Keep out of reach of children and pets.</p>
  </main>
</body>
</html>
```